Brindlewick Music Studio needs a promotional postcard design

We are looking for a postcard design for a small business that provides clients with private music lesson instruction. We are looking for a design that will convey the message of "music is fun for kids" that will appeal to parents and encourage them to sign up. We have a company logo that should be used and our color scheme is teal and turquoise. All of our contact info should be displayed as well.

Target Market(s)

Parents with young kids

Contact Information for Business Card

web: www.brindlewickmusicstudio.example
email: lessons@brindlewickmusicstudio.example
phone: 202-555-0147

Font styles to use
Serif
Sans Serif

Colors
33b8a4
86cfc6
0456a4
87cfc6

Requirements
Must have
• Music lessons in your home
• Creating little stars one at a time
• Sign Up Now
• Please use these images:
Nice to have
• Something like this sample postcard:

```html
<!DOCTYPE html>
<html lang="en">
<head>
<meta charset="utf-8">
<title>Brindlewick Music Studio – Postcard</title>
<link rel="stylesheet" href="https://fonts.googleapis.com/css2?family=Libre+Baskerville&family=Oswald:wght@500;600&family=Open+Sans:wght@400&display=swap">
<style>
  :root {
    --teal: #4bb8bf;
    --teal-deep: #3aa9b1;
    --teal-soft: #86cfc6;
    --ink: #262626;
    --stage: #2d2d2d;
    --white: #ffffff;
    --rule: #e3e3e3;
    --stamp: #f0f0f0;
  }
  * { margin: 0; padding: 0; box-sizing: border-box; }
  html, body { width: 1200px; height: 1200px; overflow: hidden; }
  body { background: var(--stage); position: relative; font-family: "Open Sans", sans-serif; }

  .card { position: absolute; background: var(--white); overflow: hidden; box-shadow: 0 4px 14px rgba(0,0,0,.45); }
  .card--front { left: 201px; top: 56px; width: 802px; height: 537px; }
  .card--back  { left: 198px; top: 614px; width: 809px; height: 540px; }

  .photo-layer { position: absolute; inset: 0; }

  .brand { position: absolute; display: flex; align-items: center; gap: 16px; }
  .brand__mark { border-radius: 50%; flex: none; }
  .brand__name { font-family: "Libre Baskerville", serif; font-weight: 400; line-height: 1.15; }

  .card--front .brand { right: 20px; top: 32px; }
  .card--front .brand__mark { width: 84px; height: 84px; border: 5px solid var(--teal); }
  .card--front .brand__name { color: var(--teal); font-size: 27px; }

  .headline { position: absolute; right: 20px; top: 166px; text-align: right;
    font-family: "Oswald", sans-serif; font-weight: 600; font-size: 66px; line-height: 68px; letter-spacing: .5px; }
  .headline__accent { color: var(--teal); display: block; }
  .headline__main { color: var(--ink); display: block; }

  .tagline { position: absolute; left: 422px; top: 304px; width: 380px; height: 54px;
    background: linear-gradient(90deg, var(--teal-soft), var(--teal)); color: var(--white);
    font-family: "Oswald", sans-serif; font-weight: 500; font-size: 24px; line-height: 54px; padding-left: 14px; }

  .cta { position: absolute; left: 420px; top: 366px; width: 362px; display: flex; align-items: center; gap: 10px;
    font-family: "Oswald", sans-serif; font-weight: 600; font-size: 29px; color: var(--ink); }
  .cta::before, .cta::after { content: ""; flex: 1; height: 3px; background: var(--teal); }

  .back-panel { position: absolute; left: 0; top: 0; width: 434px; height: 100%;
    background: radial-gradient(circle at 75% 30%, #6cc8cd 0, transparent 40%),
                radial-gradient(circle at 20% 70%, #5fc1c7 0, transparent 35%),
                var(--teal); }
  .card--back .brand { left: 23px; top: 48px; }
  .card--back .brand__mark { width: 100px; height: 100px; border: 5px solid var(--white); }
  .card--back .brand__name { color: var(--white); font-size: 33px; }

  .contact-label { position: absolute; left: 0; top: 296px; width: 201px; height: 45px; background: var(--white);
    color: var(--teal-deep); font-family: "Oswald", sans-serif; font-weight: 600; font-size: 29px; line-height: 45px; padding-left: 40px; }

  .contact-list { position: absolute; left: 42px; top: 372px; list-style: none; }
  .contact-list li { display: flex; align-items: center; gap: 7px; height: 37px; color: var(--white); font-size: 17px; }
  .contact-list svg { width: 30px; height: 30px; flex: none; }

  .stamp-box { position: absolute; left: 629px; top: 31px; width: 149px; height: 140px; background: var(--stamp); border: 1px solid #e2e2e2; }
  .address-line { position: absolute; left: 462px; width: 324px; height: 2px; background: var(--rule); }
</style>
</head>
<body>

<section class="card card--front">
  <svg class="photo-layer" width="802" height="537" viewBox="0 0 802 537">
    <defs>
      <linearGradient id="lessonTone" x1="0" y1="0" x2="1" y2="1">
        <stop offset="0" stop-color="#c9b79c"/>
        <stop offset=".45" stop-color="#3b4f8f"/>
        <stop offset="1" stop-color="#6b5a4b"/>
      </linearGradient>
      <linearGradient id="smileTone" x1="0" y1="0" x2="0" y2="1">
        <stop offset="0" stop-color="#9c7452"/>
        <stop offset="1" stop-color="#2e2a30"/>
      </linearGradient>
    </defs>
    <polygon points="0,0 399,0 223,537 0,537" fill="url(#lessonTone)" role="img" aria-label="Photo of a young girl practising violin at home"/>
    <polygon points="299,326 231,537 451,537" fill="url(#smileTone)" role="img" aria-label="Photo of a smiling girl making a peace sign"/>
  </svg>

  <div class="brand">
    <span class="brand__mark"></span>
    <span class="brand__name">Brindlewick<br>Music Studio</span>
  </div>

  <h1 class="headline">
    <span class="headline__accent">MUSIC LESSONS</span>
    <span class="headline__main">IN YOUR HOME</span>
  </h1>

  <p class="tagline">CREATING LITTLE STARS ONE AT A TIME</p>
  <p class="cta">SIGN UP NOW</p>
</section>

<section class="card card--back">
  <div class="back-panel">
    <div class="brand">
      <span class="brand__mark"></span>
      <span class="brand__name">Brindlewick<br>Music Studio</span>
    </div>

    <h2 class="contact-label">CONTACT US</h2>

    <ul class="contact-list">
      <li>
        <svg viewBox="0 0 30 30" fill="none" stroke="#fff" stroke-width="1.8">
          <circle cx="15" cy="15" r="13"/>
          <path d="M10.5 9.5c1-1 2-1 2.6 0l1 1.6c.4.7.2 1.3-.4 1.8l-.6.5c.6 1.7 1.8 2.9 3.5 3.5l.5-.6c.5-.6 1.1-.8 1.8-.4l1.6 1c1 .6 1 1.6 0 2.6-1.2 1.2-3 1.2-5.4-.6-2.2-1.6-3.8-3.4-4.8-5.5-.8-1.7-.6-3 .2-3.9z" fill="#fff" stroke="none"/>
        </svg>
        202-555-0147
      </li>
      <li>
        <svg viewBox="0 0 30 30" fill="none" stroke="#fff" stroke-width="1.8">
          <circle cx="15" cy="15" r="13"/>
          <rect x="8.5" y="10.5" width="13" height="9" rx="1" fill="#fff" stroke="none"/>
          <path d="M8.5 11l6.5 5 6.5-5" stroke="#4bb8bf" stroke-width="1.4"/>
        </svg>
        lessons@brindlewickmusicstudio.example
      </li>
      <li>
        <svg viewBox="0 0 30 30" fill="none" stroke="#fff" stroke-width="1.5">
          <circle cx="15" cy="15" r="13" stroke-width="1.8"/>
          <circle cx="15" cy="15" r="6.5"/>
          <ellipse cx="15" cy="15" rx="2.8" ry="6.5"/>
          <path d="M8.5 15h13M9.5 11.8h11M9.5 18.2h11"/>
        </svg>
        www.brindlewickmusicstudio.example
      </li>
    </ul>
  </div>

  <div class="stamp-box"></div>
  <span class="address-line" style="top:289px"></span>
  <span class="address-line" style="top:334px"></span>
  <span class="address-line" style="top:384px"></span>
  <span class="address-line" style="top:431px"></span>
  <span class="address-line" style="top:482px"></span>
</section>

</body>
</html>
```